Web design for Crowdfunding site HaloFundry.com

We need a web design for christian crowdfunding website. Here is the challenge: We need responsive layout that is targeted first in iPad size of screen. It should also scale somehow down to iPhone size of screens. Web layout can be about the same size as iPad screen.

Screens should work so that main page scrolls not but only certain part of the screen scrolls and always one "page" at time. We can implement these "scrolls" then later with javascript but now we need only design. The challenge is to create this kind of hybrid website / app look.

Target is at first to raise funds to orphan people needing about $40 per month for their living and education. There is always some organization which takes care of these kids. Later there will be other christian missions included. At first we are looking to find monthly supporters.

You can be as creative as you want :) As you see from the look and feel sector, I am not looking any same traditional look which many "help kids" sites have. I am looking to reach now younger generation and therefore iPad and mobile are the main screen sizes.

Inspirational designs:
- https://brightpixelhub.example/profiles/studiokelvira/designs/418263?from=%2Fbrowse%2Fxhr%2Fdesigns%3Fcategory%3Dmobile-app-design
- http://www.artmarketloop.example/design/7261540 Clear, simple visuals
- http://www.artmarketloop.example/design/8420917 Header
- http://www.artmarketloop.example/design/6394275 Contrast in the colors, i think is powerfull

Some terms could be: Kids play, kids are learning (in the school). No static posture but living like kids are. I wonder also how we could also add little bit gaming style even though the question is of reali life of real people. Giving should be rewarding.

Target Market(s)

People who want help other people.

Industry/Entity Type

Christian

Number of Pages Required

4 page

Requirements
Must have
• Homepage. Mission page (In my wireframes it was one kid).
Nice to have
• Other pages and some idea how to scroll. 4 pages is no must. If you feel easy, please give first some draft and I give comments on that.

```html
<!DOCTYPE html>
<html lang="en">
<head>
<meta charset="utf-8">
<title>HaloFundry – My Missions</title>
<link href="https://fonts.googleapis.com/css2?family=Lato:wght@400;700;900&family=Roboto:wght@300;400;500;700&display=swap" rel="stylesheet">
<style>
:root{
  --teal:#48c9b0;
  --ink:#1c1c1c;
  --text:#333;
  --muted:#666;
  --page:#eeeef4;
  --card:#ffffff;
  --avatar:#a9a9ab;
  --ring-track:#c9c9cc;
  --ring-box:#e7e8ea;
  --plus:#3fc85e;
  --dot:#1d7cf2;
  --rule:#d6d6dc;
}
*{box-sizing:border-box;margin:0;padding:0}
html,body{width:1200px;height:2161px;overflow:hidden}
body{position:relative;background:var(--page);font-family:'Roboto',sans-serif;color:var(--text)}
.abs{position:absolute}

/* header */
.site-header{position:absolute;left:0;top:0;width:1200px;height:113px;background:var(--teal)}
.menu-icon{position:absolute;left:27px;top:30px}
.menu-label{position:absolute;left:95px;top:48px;font:500 22px 'Lato',sans-serif;color:var(--ink);letter-spacing:.2px}
.brand{position:absolute;left:0;width:1178px;text-align:center;top:30px;font:700 38px 'Lato',sans-serif;color:var(--ink);letter-spacing:.5px}
.account-links{position:absolute;right:20px;top:40px;font:500 22px 'Lato',sans-serif;color:var(--ink)}
.account-links span{margin-left:18px}

.hero{position:absolute;left:0;top:113px;width:1200px;height:725px;
  background:radial-gradient(ellipse at 35% 55%,#b8aa98 0%,#d8cfc3 40%,#f1ede8 80%,#f7f5f2 100%)}
.hero-band{position:absolute;left:0;top:838px;width:1200px;height:76px;background:var(--teal)}

/* profile */
.profile-avatar{position:absolute;left:60px;top:924px;width:182px;height:182px}
.profile-info{position:absolute;left:303px;top:970px;font-size:20px;color:#222;line-height:41px}
.following{position:absolute;left:781px;top:970px}
.following h3{font:400 20px 'Roboto',sans-serif;color:#222;margin-bottom:8px}
.follower{display:flex;align-items:center;height:44px;font-size:20px;color:#222}
.follower svg{margin-right:14px}

.section-title{position:absolute;font:400 20px 'Roboto',sans-serif;color:#333;display:flex;align-items:center;gap:12px;letter-spacing:.3px}

/* mission cards */
.mission-card{position:absolute;width:527px;height:100px;background:var(--card);box-shadow:0 1px 2px rgba(0,0,0,.08)}
.mission-card .avatar{position:absolute;left:18px;top:13px}
.mission-card .who{position:absolute;left:110px;top:32px;font-size:19px;line-height:21px;color:#222}
.mission-card .who small{font-size:17px}
.mission-card .dot{position:absolute;left:262px;top:43px;width:15px;height:15px;border-radius:50%;background:var(--dot)}
.mission-card .stats{position:absolute;left:316px;top:10px;font-size:13px;line-height:31px;color:#222}
.mission-card .ring{position:absolute;left:385px;top:16px;width:82px;height:67px;background:var(--ring-box);border-radius:4px}
.mission-card .add{position:absolute;left:484px;top:35px}
.swipe-hint{position:absolute;left:860px;top:1418px;font-size:20px;color:#333;display:flex;align-items:center}
.swipe-hint .dots{color:#aaa;font-size:12px;margin-right:46px;letter-spacing:2px}
.swipe-hint .gap{margin-left:18px}

.rule{position:absolute;left:60px;top:1492px;width:1036px;height:2px;background:var(--rule)}

/* activities */
.activity-card{position:absolute;width:504px;height:157px;background:var(--card);padding:20px 22px 0 49px}
.activity-card .dot{position:absolute;left:18px;top:23px;width:17px;height:17px;border-radius:50%;background:var(--dot)}
.activity-card .time{position:absolute;right:40px;top:22px;font-size:16px;color:#777}
.activity-card .chev{position:absolute;right:16px;top:20px}
.activity-card .name{font-weight:700;font-size:19px;color:#222;line-height:24px}
.activity-card .subject{font-size:19px;color:#222;line-height:26px}
.activity-card .subject.bold{font-weight:700}
.activity-card .body{font-size:15px;color:#444;line-height:21px;font-weight:300}
.activity-card .clip{position:absolute;left:17px;top:50px}
.new-angel{display:flex;align-items:center;margin-top:6px}
.new-angel span{margin-left:110px;font-size:16px;color:#555}

.site-footer{position:absolute;left:0;top:2083px;width:1200px;height:78px;background:#fff}
.next-page{position:absolute;right:25px;top:26px;font:500 21px 'Roboto',sans-serif;color:#222;display:flex;align-items:center;gap:8px;letter-spacing:.3px}
</style>
</head>
<body>

<header class="site-header">
  <svg class="menu-icon" width="56" height="54" viewBox="0 0 56 54"><rect width="56" height="11" fill="#111"/><rect y="21" width="56" height="11" fill="#111"/><rect y="43" width="56" height="11" fill="#111"/></svg>
  <div class="menu-label">SEE THE MISSIONS</div>
  <div class="brand">HALOFUNDRY</div>
  <div class="account-links"><span>LOG IN</span><span>SIGN UP</span></div>
</header>

<div class="hero" role="img" aria-label="Sepia photograph of two smiling children sharing a sweet"></div>
<div class="hero-band"></div>

<svg class="profile-avatar" viewBox="0 0 182 182" aria-label="Profile avatar">
  <defs><clipPath id="pc"><circle cx="91" cy="91" r="86"/></clipPath></defs>
  <circle cx="91" cy="91" r="86" fill="#fff"/>
  <g clip-path="url(#pc)" fill="var(--avatar)">
    <ellipse cx="91" cy="72" rx="32" ry="40"/>
    <path d="M20 182 C22 135 50 118 91 118 C132 118 160 135 162 182Z"/>
  </g>
  <circle cx="91" cy="91" r="86" fill="none" stroke="var(--avatar)" stroke-width="6"/>
</svg>

<div class="profile-info">
  <div>Name: MATTHEW MATT</div>
  <div>Username: matt28</div>
</div>

<div class="following">
  <h3>FOLLOWING</h3>
  <div class="follower"><svg width="36" height="36" viewBox="0 0 36 36"><circle cx="18" cy="18" r="17" fill="#ddd" stroke="#bbb"/><circle cx="18" cy="15" r="7" fill="var(--avatar)"/><path d="M6 32c2-7 7-9 12-9s10 2 12 9z" fill="var(--avatar)"/></svg>Maria,....</div>
  <div class="follower"><svg width="36" height="36" viewBox="0 0 36 36"><circle cx="18" cy="18" r="17" fill="#ddd" stroke="#bbb"/><circle cx="18" cy="15" r="7" fill="var(--avatar)"/><path d="M6 32c2-7 7-9 12-9s10 2 12 9z" fill="var(--avatar)"/></svg>Maria,....</div>
  <div class="follower"><svg width="36" height="36" viewBox="0 0 36 36"><circle cx="18" cy="18" r="17" fill="#ddd" stroke="#bbb"/><circle cx="18" cy="15" r="7" fill="var(--avatar)"/><path d="M6 32c2-7 7-9 12-9s10 2 12 9z" fill="var(--avatar)"/></svg>Maria,....</div>
</div>

<div class="section-title" style="left:52px;top:1115px">MY MISSIONS
  <svg width="22" height="14" viewBox="0 0 22 14"><path d="M1 2l10 10 10-10" fill="none" stroke="#aaa" stroke-width="1.6"/></svg></div>

<svg width="0" height="0" style="position:absolute">
  <defs>
    <symbol id="kid-avatar" viewBox="0 0 74 74">
      <circle cx="37" cy="37" r="35" fill="#fff" stroke="var(--avatar)" stroke-width="2.5"/>
      <clipPath id="kc"><circle cx="37" cy="37" r="33"/></clipPath>
      <g clip-path="url(#kc)" fill="var(--avatar)"><ellipse cx="37" cy="31" rx="14" ry="17"/><path d="M8 74c2-18 14-24 29-24s27 6 29 24z"/></g>
    </symbol>
    <symbol id="progress-ring" viewBox="0 0 82 67">
      <circle cx="41" cy="33.5" r="24" fill="#fff" stroke="var(--ring-track)" stroke-width="5"/>
      <circle cx="41" cy="33.5" r="24" fill="none" stroke="var(--teal)" stroke-width="5" stroke-dasharray="90 151" transform="rotate(-90 41 33.5)"/>
      <text x="41" y="38" text-anchor="middle" font-family="Roboto,sans-serif" font-size="13" fill="#999">45°</text>
    </symbol>
    <symbol id="add-button" viewBox="0 0 30 30">
      <circle cx="15" cy="15" r="15" fill="var(--plus)"/><path d="M15 8v14M8 15h14" stroke="#fff" stroke-width="3"/>
    </symbol>
    <symbol id="chevron-right" viewBox="0 0 10 14"><path d="M2 1l6 6-6 6" fill="none" stroke="#999" stroke-width="1.4"/></symbol>
  </defs>
</svg>

<!-- mission cards, left column -->
<div class="mission-card" style="left:52px;top:1154px">
  <svg class="avatar" width="74" height="74"><use href="#kid-avatar"/></svg>
  <div class="who">Maria, 11y<br>Orphan, Jacob</div>
  <span class="dot"></span>
  <div class="stats">$15 raised<br>$20 to go<br>5 angels in</div>
  <svg class="ring"><use href="#progress-ring"/></svg>
  <svg class="add" width="30" height="30"><use href="#add-button"/></svg>
</div>
<div class="mission-card" style="left:52px;top:1257px">
  <svg class="avatar" width="74" height="74"><use href="#kid-avatar"/></svg>
  <div class="who">Matthew, 11y<br>Orphan, Jacob</div>
  <div class="stats">$15 raised<br>$20 to go<br>5 angels in</div>
  <svg class="ring"><use href="#progress-ring"/></svg>
  <svg class="add" width="30" height="30"><use href="#add-button"/></svg>
</div>
<div class="mission-card" style="left:52px;top:1360px">
  <svg class="avatar" width="74" height="74"><use href="#kid-avatar"/></svg>
  <div class="who">Maria, 11y<br><small>Orphan, Jacob</small></div>
  <span class="dot"></span>
  <div class="stats">$15 raised<br>$20 to go<br>5 angels in</div>
  <svg class="ring"><use href="#progress-ring"/></svg>
  <svg class="add" width="30" height="30"><use href="#add-button"/></svg>
</div>

<!-- mission cards, right column -->
<div class="mission-card" style="left:613px;top:1154px">
  <svg class="avatar" width="74" height="74"><use href="#kid-avatar"/></svg>
  <div class="who">Maria, 11y<br>Orphan, Jacob</div>
  <svg class="ring"><use href="#progress-ring"/></svg>
  <svg class="add" width="30" height="30"><use href="#add-button"/></svg>
</div>
<div class="mission-card" style="left:613px;top:1257px">
  <svg class="avatar" width="74" height="74"><use href="#kid-avatar"/></svg>
  <div class="who">Matthew, 11y<br>Orphan, Jacob</div>
  <div class="stats">$15 raised<br>$20 to go<br>5 angels in</div>
  <svg class="ring"><use href="#progress-ring"/></svg>
  <svg class="add" width="30" height="30"><use href="#add-button"/></svg>
</div>

<div class="swipe-hint"><span class="dots">○○○</span>Swipe to<span class="gap">see more?</span></div>

<div class="rule"></div>
<div class="section-title" style="left:63px;top:1494px">ACTIVITIES
  <svg width="14" height="24" viewBox="0 0 14 24"><path d="M2 2l10 10-10 10" fill="none" stroke="#aaa" stroke-width="1.6"/></svg></div>

<!-- activities -->
<article class="activity-card" style="left:60px;top:1532px">
  <span class="dot"></span><span class="time">10:51 AM</span>
  <svg class="chev" width="10" height="14"><use href="#chevron-right"/></svg>
  <svg class="clip" width="16" height="16" viewBox="0 0 16 16"><path d="M11 4L5 10a2 2 0 0 0 3 3l6-6a3.5 3.5 0 0 0-5-5L3 8" fill="none" stroke="#999" stroke-width="1.3"/></svg>
  <div class="name">Maria</div>
  <div class="subject bold">Report</div>
  <div class="body">Half year report.....</div>
</article>
<article class="activity-card" style="left:575px;top:1532px;padding-left:49px">
  <span class="dot"></span><span class="time">10:51 AM</span>
  <svg class="chev" width="10" height="14"><use href="#chevron-right"/></svg>
  <div class="name">Maria</div>
  <div class="subject bold">Got a new angel</div>
  <div class="new-angel"><svg width="74" height="74"><use href="#kid-avatar"/></svg><span>Anonymous</span></div>
</article>

<article class="activity-card" style="left:60px;top:1693px">
  <span class="dot"></span><span class="time">10:51 AM</span>
  <svg class="chev" width="10" height="14"><use href="#chevron-right"/></svg>
  <div class="name">Imma Mustard</div>
  <div class="subject">This is and important message</div>
  <div class="body">Lorem ipsum dolor sit amet, sapien etiam, nunc amet dolor ac odio mauris justo. dolor sit amet, sapien etiam, nunc amet dolor ac odio mauris justo Luctus...</div>
</article>
<article class="activity-card" style="left:575px;top:1693px">
  <span class="dot"></span><span class="time">10:51 AM</span>
  <svg class="chev" width="10" height="14"><use href="#chevron-right"/></svg>
  <div class="name">Matthew</div>
  <div class="subject bold">Prayer request</div>
  <div class="body">Lorem ipsum dolor sit amet, sapien etiam, nunc amet dolor ac odio mauris justo. dolor sit amet, sapien etiam, nunc amet dolor ac odio mauris justo Luctus...</div>
</article>

<article class="activity-card" style="left:60px;top:1854px">
  <span class="dot"></span><span class="time">10:51 AM</span>
  <svg class="chev" width="10" height="14"><use href="#chevron-right"/></svg>
  <div class="name">Imma Mustard</div>
  <div class="subject">This is and important message</div>
  <div class="body">Lorem ipsum dolor sit amet, sapien etiam, nunc amet dolor ac odio mauris justo. dolor sit amet, sapien etiam, nunc amet dolor ac odio mauris justo Luctus...</div>
</article>
<article class="activity-card" style="left:575px;top:1854px">
  <span class="dot"></span><span class="time">10:51 AM</span>
  <svg class="chev" width="10" height="14"><use href="#chevron-right"/></svg>
  <div class="name">Matthew</div>
  <div class="subject bold">Prayer request</div>
  <div class="body">Lorem ipsum dolor sit amet, sapien etiam, nunc amet dolor ac odio mauris justo. dolor sit amet, sapien etiam, nunc amet dolor ac odio mauris justo Luctus...</div>
</article>

<footer class="site-footer">
  <div class="next-page">NEXT PAGE
    <svg width="18" height="16" viewBox="0 0 18 16"><path d="M2 2l6 6-6 6M9 2l6 6-6 6" fill="none" stroke="#222" stroke-width="1.8"/></svg></div>
</footer>

</body>
</html>
```